Digital Price Menus for Detail Shop

I am looking to have digital menus for my detail shop. I have 3 55-inch TVs (see pictures) on how they are situated on the wall for my front desk area. They will be vertical, not horizontal.

Color pallet I am looking for is black and gold, with some accent colors if applicable. I would like black background with some sort of design in it in such a way it looks faint or ghosted in the background ... i.e., honeycomb, splatter, etc. A boarder is optional.

Needs to be designed well, organized well and easy to read for customers walking in.

the each document is for each TV, Interior, Exterior and Ceramic Coatings

Company logo files included. would like my logos on them as well

Target Market(s)

Customers walking in to my shop, easy to read and understand

Industry/Entity Type

Car wash, Detailing

Colors

Designer to choose only greyscale colors for use in the design.

Requirements
Nice to have
• Professional Look
Should not have
• tacky look

```html
<!DOCTYPE html>
<html lang="en">
<head>
<meta charset="utf-8">
<title>Lumen Garage – Digital Price Menus</title>
<link href="https://fonts.googleapis.com/css2?family=Poppins:wght@400;500;600;700;800&family=Montserrat:wght@400;500;600;700&display=swap" rel="stylesheet">
<style>
:root{
  --page:#ffffff;
  --black:#0b0b0b;
  --panel-top:#151515;
  --white:#f4f4f4;
  --muted:#bdbdbd;
  --gold:#c9a24a;
  --gold-light:#f0d58a;
  --gold-dark:#7d5d22;
  --gold-grad:linear-gradient(180deg,#f3dc93 0%,#d2ab55 45%,#a67c30 100%);
  --band-grad:linear-gradient(90deg,#7d5d22 0%,#c9a04c 22%,#f1d88f 50%,#c79b42 78%,#7d5d22 100%);
}
*{box-sizing:border-box;margin:0;padding:0}
html,body{width:1200px;height:2400px;overflow:hidden;background:var(--page)}
body{position:relative;font-family:"Montserrat",sans-serif;color:var(--white)}

.menu{position:absolute;width:560px;height:990px;background:radial-gradient(ellipse at 70% 10%,var(--panel-top) 0%,var(--black) 60%);overflow:hidden}
.menu--exterior{left:320px;top:150px}
.menu--ceramic{left:20px;top:1260px}
.menu--interior{left:620px;top:1260px}
.menu__pattern{position:absolute;inset:0;background:linear-gradient(135deg,rgba(201,162,74,.07) 0%,transparent 35%,transparent 65%,rgba(201,162,74,.06) 100%)}

/* header */
.brand{position:absolute;left:44px;top:50px;width:130px;text-align:center}
.brand__mark{width:44px;height:44px;border:2px solid var(--white);border-radius:50%;margin:0 auto 8px}
.brand__name{font-family:"Poppins",sans-serif;font-weight:600;font-size:17px;letter-spacing:1px;color:var(--white);line-height:1.1}
.brand__tag{font-family:"Poppins",sans-serif;font-weight:600;font-size:6.5px;letter-spacing:1px;color:var(--white);margin-top:3px}
.title{position:absolute;right:30px;top:38px;width:290px;text-align:center}
.title__main{font-family:"Poppins",sans-serif;font-weight:800;font-size:50px;line-height:.98;letter-spacing:.5px;background:var(--gold-grad);-webkit-background-clip:text;background-clip:text;color:transparent}
.title__sub{display:flex;align-items:center;justify-content:center;gap:10px;margin-top:4px;font-family:"Poppins",sans-serif;font-size:17px;letter-spacing:7px;color:var(--white)}
.title__sub::before,.title__sub::after{content:"";width:30px;height:1px;background:var(--gold)}

/* shared pieces */
.dots{display:block;text-align:center;color:var(--gold);font-size:8px;letter-spacing:2px;line-height:1}
.dots::before{content:"• • •"}
.section-head{position:absolute;left:0;right:0;text-align:center;font-family:"Poppins",sans-serif;font-weight:600;font-size:15px;color:var(--white)}
.section-head--gold{color:var(--gold);font-size:20px;font-weight:600}
.box{position:absolute;border:1px solid var(--gold);}
.box__title{position:absolute;top:-10px;left:50%;transform:translateX(-50%);background:var(--black);padding:0 6px;white-space:nowrap;font-family:"Poppins",sans-serif;font-weight:600;font-size:13px;color:var(--white)}
.price{font-family:"Poppins",sans-serif;font-weight:600;font-size:24px;color:var(--gold);line-height:1;display:inline-flex;align-items:center;gap:3px}
.price small{font-size:7px;line-height:1;color:var(--white);font-weight:600}
.label{font-family:"Poppins",sans-serif;font-size:11px;color:var(--white)}
.small-text{font-size:8.5px;line-height:1.35;color:var(--muted)}

/* exterior package boxes */
.pkg{width:226px;height:142px;display:flex;padding:24px 14px 10px 20px;gap:12px}
.pkg__prices{width:70px;display:flex;flex-direction:column;gap:2px}
.pkg__prices .label{margin-top:2px}
.checks{list-style:none;flex:1}
.checks li{position:relative;padding-left:11px;font-size:7px;line-height:1.55;color:var(--white)}
.checks li::before{content:"";position:absolute;left:0;top:2px;width:7px;height:7px;border-radius:50%;background:var(--gold)}
.checks li::after{content:"";position:absolute;left:2.3px;top:3.4px;width:2px;height:3px;border:solid var(--black);border-width:0 1px 1px 0;transform:rotate(45deg)}
.checks--dense li{font-size:6.5px;line-height:1.4}
.checks--text li{padding-left:0}
.checks--text li::before,.checks--text li::after{display:none}

.band{position:absolute;background:var(--band-grad);color:#1a1408;text-align:center}
.band__tab{position:absolute;top:0;left:50%;transform:translateX(-50%);background:var(--black);color:var(--white);font-family:"Poppins",sans-serif;font-weight:600;font-size:13px;padding:3px 12px}

.addons{position:absolute;left:50px;right:50px;display:grid;grid-template-columns:1fr 1fr;row-gap:20px;column-gap:30px}
.addon{display:flex;align-items:center;gap:8px}
.addon svg{width:22px;height:22px;flex:none}
.addon__name{flex:1;font-family:"Poppins",sans-serif;font-weight:500;font-size:10px;line-height:1.2}
.addon__name span{display:block;font-family:"Montserrat",sans-serif;font-weight:400;font-size:7px;color:var(--muted)}
.addon .price{font-size:20px}

.extras{left:34px;right:34px;top:832px;height:120px;display:grid;grid-template-columns:1fr 1.3fr 1fr}
.extras__col{padding:22px 10px 0;text-align:center}
.extras__col+.extras__col{border-left:1px solid rgba(201,162,74,.6)}
.extras__name{font-family:"Poppins",sans-serif;font-weight:500;font-size:11px;color:var(--gold);line-height:1.2;margin-bottom:3px}
.extras .small-text{font-size:7.5px;margin-top:4px}

/* ceramic */
.intro{position:absolute;left:40px;right:40px;text-align:center;font-size:10px;line-height:1.35;color:var(--white)}
.tiers{position:absolute;left:34px;right:34px;display:flex;gap:24px}
.tier{position:relative;flex:1;height:204px;border:1px solid var(--gold);text-align:center;padding-top:38px}
.tier__badge{position:absolute;top:-6px;left:50%;transform:translateX(-50%);background:var(--gold);color:var(--black);font-family:"Poppins",sans-serif;font-weight:600;font-size:12px;padding:0 6px;white-space:nowrap}
.tier__badge b{font-size:22px;font-weight:700}
.tier__kind{font-family:"Poppins",sans-serif;font-size:13px;letter-spacing:3px;margin-top:4px}
.tier__from{font-size:10px;margin-top:8px}
.tier .price{font-size:28px;margin:2px 0 6px}
.tier p{font-size:8px;line-height:1.3;color:var(--white);padding:0 10px}

.rows{position:absolute;left:34px;right:34px}
.row{display:flex;align-items:center;min-height:76px}
.row__info{flex:1;padding-right:20px}
.row__name{font-family:"Poppins",sans-serif;font-weight:600;font-size:12.5px;color:var(--white)}
.row__info .dots{text-align:left;font-size:6px;margin:3px 0 4px}
.row__info .small-text{font-size:8.5px;color:var(--white)}
.row__divider{width:2px;height:54px;background:linear-gradient(180deg,transparent,var(--gold),transparent);position:relative}
.row__divider::after{content:"";position:absolute;left:-2px;top:50%;width:6px;height:6px;border-right:1px solid var(--gold);border-bottom:1px solid var(--gold);transform:translateY(-50%) rotate(-45deg)}
.row__price{width:120px;padding-left:34px}
.row__price .label{font-size:10px}
.row__price .price{font-size:26px}

/* interior */
.services{position:absolute;left:34px;right:34px;top:640px;display:grid;grid-template-columns:1fr 1fr;column-gap:42px;row-gap:42px}
.service{position:relative;height:92px;border:1px solid var(--gold);text-align:center;padding-top:26px}
.service .box__title{top:-10px;font-size:13px;line-height:1.2;white-space:normal;width:170px}
.service .small-text{font-size:8px;color:var(--white);padding:0 20px}
.service .price{font-size:26px;margin-top:6px}
.service--tall{padding-top:40px}
.surcharge{position:absolute;left:34px;right:34px;top:922px;height:34px;display:flex;align-items:center;border-bottom:1px solid var(--gold)}
.surcharge__label{height:34px;display:flex;align-items:center;padding:0 40px 0 14px;background:var(--band-grad);clip-path:polygon(0 0,100% 0,88% 100%,0 100%);font-family:"Poppins",sans-serif;font-weight:600;font-size:12px;color:#1a1408}
.surcharge__value{margin-left:22px;font-family:"Poppins",sans-serif;font-weight:600;font-size:15px;color:var(--gold)}
</style>
</head>
<body>

<!-- EXTERIOR -->
<section class="menu menu--exterior">
  <div class="menu__pattern" role="img" aria-label="Faint gold geometric line network across the black background"></div>
  <div class="brand"><div class="brand__mark"></div><div class="brand__name">LUMEN GARAGE</div><div class="brand__tag">DETAILING &amp; COATINGS</div></div>
  <div class="title"><h1 class="title__main">EXTERIOR<br>DETAILING</h1><div class="title__sub">PACKAGES</div></div>

  <div class="box pkg" style="left:34px;top:186px">
    <div class="box__title">HAND WASH</div>
    <div class="pkg__prices">
      <span class="label">Cars</span><span class="price">50</span>
      <span class="label">Trucks/SUVS</span><span class="price">60<small>and<br>up</small></span>
    </div>
    <ul class="checks"><li>Presoak</li><li>Foam Bath</li><li>Bug Removal</li><li>Wheels Cleaned</li><li>Tires Dressed</li><li>Exterior Glass Cleaned</li><li>Blow Dried</li><li>Add Spray Wax for $20</li></ul>
  </div>
  <div class="box pkg" style="right:34px;top:186px">
    <div class="box__title">COMPLETE EXTERIOR DETAIL</div>
    <div class="pkg__prices">
      <span class="label">Cars</span><span class="price">180</span>
      <span class="label">Trucks/SUVS</span><span class="price">220<small>and<br>up</small></span>
    </div>
    <ul class="checks"><li>Standard Hand Wash plus:</li><li>Iron Decon &amp; Clay Bar</li><li>Door jams/Trunk Lid/ Gas Cap Cleaned</li><li>Tires/Trim Dressed</li><li>Hand Applied Wax</li><li>*DOES NOT REMOVE SCRATCHES*</li></ul>
  </div>

  <div class="section-head section-head--gold" style="top:358px">NEED SCRATCHES AND SWIRLS REMOVED?<span class="dots"></span></div>

  <div class="box pkg" style="left:34px;top:410px">
    <div class="box__title">PAINT ENHANCEMENT</div>
    <div class="pkg__prices">
      <span class="label">Cars</span><span class="price">350</span>
      <span class="label">Trucks/SUVS</span><span class="price">400<small>and<br>up</small></span>
    </div>
    <ul class="checks checks--dense"><li>Complete Exterior Detail PLUS:</li><li>One-step Polish To Deep Clean The Paint, Reduce Swirls and Increase Gloss</li><li>Windshield is Protected with Dropvane</li><li>Paint Work is Protected with a Ceramic Sealant (Protects 6mo) Paint Correction</li></ul>
  </div>
  <div class="box pkg" style="right:34px;top:410px">
    <div class="box__title">PAINT CORRECTION</div>
    <div class="pkg__prices">
      <span class="label">Cars</span><span class="price">500</span>
      <span class="label">Trucks/SUVS</span><span class="price">600<small>and<br>up</small></span>
    </div>
    <ul class="checks checks--text"><li>Our paint enhancement PLUS paint receives a 2-step correction process to safely remove swirls, defects, and minor scratches, achieving 80% or better appearance</li></ul>
  </div>

  <div class="band" style="left:34px;right:34px;top:582px;height:88px;padding-top:32px">
    <div class="band__tab">RESTORATIVE DETAIL</div>
    <p style="font-family:Poppins,sans-serif;font-weight:600;font-size:9.5px">HAVE AN OLD, CLASSIC OR JUST PLAIN ODDBALL CAR?</p>
    <p style="font-size:8px;line-height:1.3;padding:2px 20px 0;font-weight:500">Some circumstances like single stage, vintage or patina paint doesn't fall under any of our packages but we can service anything! This type of job will require a consultation to go over the vehicle thoroughly and set a plan of action.</p>
  </div>

  <div class="section-head" style="top:696px">EXTERIOR ADD-ONS<span class="dots"></span></div>
  <div class="addons" style="top:732px">
    <div class="addon">
      <svg viewBox="0 0 24 24" fill="none" stroke="#c9a24a" stroke-width="1.6"><circle cx="12" cy="12" r="10"/><circle cx="12" cy="12" r="4"/><path d="M12 2v6M12 16v6M2 12h6M16 12h6"/></svg>
      <div class="addon__name">Complete Wheel Detail<span>Wheels off, deep cleaned and protected inside and out, reinstalled to factory spec.</span></div>
      <span class="price">150</span>
    </div>
    <div class="addon">
      <svg viewBox="0 0 24 24" fill="none" stroke="#c9a24a" stroke-width="1.6"><path d="M12 3c4 5 6 8 6 11a6 6 0 0 1-12 0c0-3 2-6 6-11z"/></svg>
      <div class="addon__name">Water Spot Removal</div>
      <span class="price">50<small>and<br>up</small></span>
    </div>
    <div class="addon">
      <svg viewBox="0 0 24 24" fill="none" stroke="#c9a24a" stroke-width="1.6"><ellipse cx="12" cy="12" rx="10" ry="7"/><circle cx="10" cy="12" r="3"/></svg>
      <div class="addon__name">Headlight Restoration</div>
      <span class="price">100<small>and<br>up</small></span>
    </div>
    <div class="addon">
      <svg viewBox="0 0 24 24" fill="none" stroke="#c9a24a" stroke-width="1.6"><path d="M20 12a8 8 0 1 1-3-6.2"/><path d="M17 2v4h-4"/></svg>
      <div class="addon__name">Plastic Trim Restoration</div>
      <span class="price">50<small>and<br>up</small></span>
    </div>
  </div>

  <div class="box extras">
    <div class="extras__col"><div class="extras__name">Scratch<br>Removal</div><span class="dots"></span><p class="small-text">Consultation required before job</p></div>
    <div class="extras__col"><div class="extras__name">Paneward Window<br>Protection</div><span class="dots"></span><p class="small-text">$100/Windshield, $150 all windows: Glass surface(s) prepped and polished. 3-year warrantied protection plan with quarterly maintenance for free</p></div>
    <div class="extras__col"><div class="extras__name">Engine Bay<br>Cleaning:</div><span class="price" style="font-size:20px">50<small>and<br>up</small></span><p class="small-text">Degreased and dressed. Waiver MUST BE signed and completed prior to work being performed</p></div>
  </div>
</section>

<!-- CERAMIC -->
<section class="menu menu--ceramic">
  <div class="menu__pattern" role="img" aria-label="Faint gold geometric line network across the black background"></div>
  <div class="brand"><div class="brand__mark"></div><div class="brand__name">LUMEN GARAGE</div><div class="brand__tag">DETAILING &amp; COATINGS</div></div>
  <div class="title"><h1 class="title__main">CERAMIC<br>COATINGS</h1><div class="title__sub">PACKAGES</div></div>

  <p class="intro" style="top:186px">All ceramic coating packages start with a Paint enhancement package. The 1 step polish will improve the appearance of blemishes, light marring and scratching 50-70%. On new cars it will reach up to 95%+ improvement. A full paint correction can be added for an additional cost. Day of pick up, a Sealant is applied to all coated surfaces to help with the curing process</p>

  <div class="band" style="left:34px;right:34px;top:268px;height:74px;display:flex;align-items:center;justify-content:center;padding:0 20px">
    <p style="font-size:10px;line-height:1.3;font-weight:500">Not every customer has the same goals when it comes to coatings so we have developed 3 different levels to choose from depending on your wants and needs and budget.</p>
  </div>

  <div class="tiers" style="top:385px">
    <div class="tier"><div class="tier__badge"><b>1</b> YEAR</div><div class="tier__kind">COATING</div><span class="dots"></span><div class="tier__from">Starting at</div><div class="price">600</div><p>applied to all painted surfaces, provides up to 12months of durability. Add a second layer for $600 more for 18-24 months of protection</p></div>
    <div class="tier"><div class="tier__badge"><b>3</b> YEAR</div><div class="tier__kind">COATING</div><span class="dots"></span><div class="tier__from">Starting at</div><div class="price">850</div><p>applied to all painted surfaces, provides up to 36 months of durability</p></div>
    <div class="tier"><div class="tier__badge"><b>5</b> YEAR</div><div class="tier__kind">COATING</div><span class="dots"></span><div class="tier__from">Starting at</div><div class="price">1100</div><p>, warrantied paint coating, applied to all painted surfaces, provides up to 60 months of durability</p></div>
  </div>

  <div class="section-head" style="top:628px;left:34px;right:34px;font-size:14px;line-height:1.3">DURABILITY IS DIRECTLY RELATED TO THE PROPER MAINTENANCE OF THE COATINGS<span class="dots"></span></div>

  <div class="rows" style="top:700px">
    <div class="row"><div class="row__info"><div class="row__name">GLASS CERAMIC COATING:</div><span class="dots"></span><p class="small-text">Ceramic Coating applied to all exterior glass panes</p></div><div class="row__divider"></div><div class="row__price"><div class="label">Starting at</div><span class="price">100</span></div></div>
    <div class="row" style="margin-top:12px"><div class="row__info"><div class="row__name">WHEEL FACE COATING</div><span class="dots"></span><p class="small-text">Wheel face coated with one layer of ceramic giving you up to 9-12 months of protection. 2 layers will yield 18+ of protection. *Raw aluminum wheels CAN NOT be coated.</p></div><div class="row__divider"></div><div class="row__price"><span class="price">100<small>wheel<br>and up</small></span></div></div>
    <div class="row" style="margin-top:12px"><div class="row__info"><div class="row__name">WHEEL OFF COATING</div><span class="dots"></span><p class="small-text">Wheel coating package + durable industrial coating on barrels of wheels and if applicable, calipers and suspension components</p></div><div class="row__divider"></div><div class="row__price"><span class="price">250<small>wheel<br>and up</small></span></div></div>
  </div>
</section>

<!-- INTERIOR -->
<section class="menu menu--interior">
  <div class="menu__pattern" role="img" aria-label="Faint gold geometric line network across the black background"></div>
  <div class="brand"><div class="brand__mark"></div><div class="brand__name">LUMEN GARAGE</div><div class="brand__tag">DETAILING &amp; COATINGS</div></div>
  <div class="title"><h1 class="title__main">INTERIOR<br>DETAILING</h1><div class="title__sub">PACKAGES</div></div>

  <p class="intro" style="top:206px">As a reminder, we would appreciate all personal items be removed from interior There may be instances were stains and pet hair are not fully removed, please understand we will do our best to remove as much as possible</p>

  <div class="rows" style="top:306px">
    <div class="row"><div class="row__info"><div class="row__name">BASIC INTERIOR CLEAN</div><span class="dots"></span><p class="small-text">Full vacuum of carpet, seats, upholstery, Floormats extracted and steam cleaned, dash/doors wiped and dressed, interior glass surfaces cleaned, center console steam cleaned</p></div><div class="row__divider"></div><div class="row__price"><span class="price">100<small>and<br>up</small></span></div></div>
    <div class="row" style="margin-top:16px"><div class="row__info"><div class="row__name">DELUXE INTERIOR CLEAN</div><span class="dots"></span><p class="small-text">Basic interior package + Full steam clean and shampoo of all interior carpet and seats, leather is gently steamed and scrubbed lightly, dash/doors/vents are dusted and dressed, steering wheel and controls are deep cleaned and dressed. Headliner/visors are lightly cleaned * Heavily soiled interiors that exceed a Deluxe Package will be charged extra</p></div><div class="row__divider"></div><div class="row__price"><span class="price">200<small>and<br>up</small></span></div></div>
    <div class="row" style="margin-top:16px"><div class="row__info"><div class="row__name">DEEP LEATHER CLEANING AND CONDITIONING</div><span class="dots"></span><p class="small-text">Deluxe interior package + premium leather conditioning treatment</p></div><div class="row__divider"></div><div class="row__price"><span class="price">100<small>Per<br>row</small></span></div></div>
  </div>

  <div class="services">
    <div class="service"><div class="box__title">BIOHAZARD CLEANING</div><p class="small-text">Plus Deluxe Interior Package</p><span class="price">350<small>Per<br>row</small></span></div>
    <div class="service"><div class="box__title">FABRIC GUARD</div><p class="small-text">and Fabric upholstery sprayed for stain and waterproofing</p><span class="price">100<small>Per<br>row</small></span></div>
    <div class="service"><div class="box__title">OZONE TREATMENT<br>FOR ODORS</div><p class="small-text" style="margin-top:10px">to remove musty, smokey odors</p><span class="price">50<small>to any<br>package</small></span></div>
    <div class="service service--tall"><div class="box__title">TRUNK AREA<br>DETAIL</div><span class="price">50<small>and<br>up</small></span></div>
  </div>

  <div class="surcharge"><div class="surcharge__label">EXCESSIVE PET HAIR REMOVAL:</div><div class="surcharge__value">10% SURCHARGE OF TOTAL</div></div>
</section>

</body>
</html>
```